Content developers BC and Stationary
Nubra نبراس
Content developers BC and Stationary - Corporate Services
Creative Brief
Simple
Rana T alMuttairi
Creative Director
Jeddah
rana@nubraco.com
for second partner, with Arabic on the back: Khaled Naji خالد ناجي Managing Director المدير التنفيذي +966507213690 +٩٦٦٥٠٧٢١٣٦٩٠ k@nubraco.com
رنا طارق المطيري المدير الإبداعي +٩٦٦٥٠٨٤٤١٢٥٩ rana@nubraco.com
Concepts
Business Cards and Stationery for new compliance company.
Business Cards and Stationery for Background Check Company

```html
<!DOCTYPE html>
<html lang="en">
<head>
<meta charset="utf-8">
<title>Nubra – Business Card</title>
<link rel="stylesheet" href="https://fonts.googleapis.com/css2?family=Open+Sans:wght@400;600;700&display=swap">
<style>
  :root {
    --page-bg: #e4e2e0;
    --card-frost: #eef0f1;
    --panel-purple: #8a5cad;
    --arc-blue: #35389a;
    --brand-purple: #7a4ea3;
    --panel-text: #ffffff;
    --panel-text-soft: #efe6f6;
  }
  * { margin: 0; padding: 0; box-sizing: border-box; }
  html, body {
    width: 1200px; height: 768px; overflow: hidden;
    background: var(--page-bg);
    font-family: "Open Sans", Arial, sans-serif;
  }
  .card {
    position: absolute; left: 150px; top: 96px;
    width: 900px; height: 576px;
    background: var(--card-frost);
    border-radius: 14px;
    overflow: hidden;
    box-shadow: 0 18px 40px rgba(60, 50, 70, 0.18);
  }
  .card-shapes { position: absolute; inset: 0; }
  .brand {
    position: absolute; left: 70px; top: 240px;
    display: flex; align-items: center; gap: 18px;
    color: var(--brand-purple);
    font-weight: 700; font-size: 78px; letter-spacing: 1px;
  }
  .brand-dot {
    width: 22px; height: 22px; border-radius: 50%;
    background: var(--brand-purple);
  }
  .contact-panel {
    position: absolute; left: 540px; top: 0; width: 340px; height: 100%;
    color: var(--panel-text);
  }
  .person-name { position: absolute; top: 92px; font-size: 27px; font-weight: 600; }
  .person-role { position: absolute; top: 132px; font-size: 21px; color: var(--panel-text-soft); }
  .address { position: absolute; top: 230px; font-size: 20px; line-height: 30px; }
  .contact-list {
    position: absolute; top: 372px; list-style: none;
    font-size: 17px; line-height: 30px;
  }
  .contact-list li { display: flex; align-items: center; gap: 10px; }
  .contact-list svg { width: 16px; height: 16px; fill: var(--panel-text); }
</style>
</head>
<body>
  <main class="card">
    <svg class="card-shapes" viewBox="0 0 900 576" width="900" height="576" aria-hidden="true">
      <path d="M495 0 L900 0 L900 576 L495 576 Q440 288 495 0 Z" fill="var(--panel-purple)"/>
      <path d="M478 -4 Q398 300 492 580" fill="none" stroke="var(--arc-blue)" stroke-width="7"/>
    </svg>

    <div class="brand">
      <span class="brand-name">Nubra</span>
      <span class="brand-dot"></span>
    </div>

    <section class="contact-panel">
      <h1 class="person-name">Marlo Quinn-Avery</h1>
      <p class="person-role">consultant</p>
      <p class="address">047 12th floor,Harbor Crest<br>Road LKN</p>
      <ul class="contact-list">
        <li><svg viewBox="0 0 16 16"><path d="M3 1h3l1.5 4-2 1.3a9 9 0 0 0 4.2 4.2L11 8.5l4 1.5v3c0 1-1 2-2 2C6.5 15 1 9.5 1 3c0-1 1-2 2-2z"/></svg>014 275 3390</li>
        <li><svg viewBox="0 0 16 16"><path d="M4.5 0h7a1 1 0 0 1 1 1v14a1 1 0 0 1-1 1h-7a1 1 0 0 1-1-1V1a1 1 0 0 1 1-1zm1 2v10h5V2zm2.5 11a1 1 0 1 0 0 2 1 1 0 0 0 0-2z"/></svg>014 275 3391</li>
        <li><svg viewBox="0 0 16 16"><path d="M4 1h8v4H4zM1 6h14v7h-3v2H4v-2H1zm4 4v4h6v-4z"/></svg>014 275 3392</li>
        <li><svg viewBox="0 0 16 16"><path d="M1 3h14v10H1zm1.5 1.2V5l5.5 4 5.5-4v-.8L8 8z"/></svg>name@nubramail.com</li>
        <li><svg viewBox="0 0 16 16"><path d="M8 1a7 7 0 1 0 0 14A7 7 0 0 0 8 1zm0 1.5c.9 0 1.8 1.9 2 4.5H6c.2-2.6 1.1-4.5 2-4.5zM2.6 7h2c.1-1.7.5-3.2 1-4.1A5.5 5.5 0 0 0 2.6 7zm8.8 0h2a5.5 5.5 0 0 0-3-4.1c.5.9.9 2.4 1 4.1zM2.6 9a5.5 5.5 0 0 0 3 4.1c-.5-.9-.9-2.4-1-4.1zm3.4 0c.2 2.6 1.1 4.5 2 4.5s1.8-1.9 2-4.5zm5.4 0c-.1 1.7-.5 3.2-1 4.1a5.5 5.5 0 0 0 3-4.1z"/></svg>www.nubrasite.com</li>
      </ul>
    </section>
  </main>
</body>
</html>
```